National Brochure Design Project

We are looking for a brochure design which will be used for a National retailer within the plumbing home improvement market.
The brochure is used to promote products which are available to order in, therefore the key theme of the brochure is 'inspiration'. Our order in range is typically higher end product so we are looking for a clean, modern layout that will showcase our extended product ranges.

The industry in which we play has a vast range of products which we can order in, therefore the layout needs to be flexible to allow for pages where multiple small products can be displayed and pages where only few larger products can be displayed as image sizes will vary.

The main message this brochure should communicate is more choice through using inspirational images and a modern design which will showcase our top end order in products.

Target Market(s)

Our target market is the household female who shops based on inspiration and feelings rather than just product information.

Industry/Entity Type

Home Improvement

Requirements
Must have
• The brochure must be an A4 landscape design (210h x 260w mm).
At the bottom of each page there must be a footer 20mm high across the entire page width, this must appear on all pages and must be orange. Orange is the corporate colour and can be used where appropriate in the design.

Font used should be Arial for the main copy within the brochure, cover/title/subheading font can differ but must still be esily legible.

On the front cover, the brochure title/heading must appear in the top 1/3rd of the page and a rectangle logo (White, 50h x 32w mm - or to scale of this size) needs to be included into this same space.

The design must include the following pages:
- A front cover (Inspirational image/s with talent is preferred) (Page 1)
- Contents and ordering information page (Page 2) (Image/s can be used if within the design concept)
- (Page 3) This is the first page which introduces the brochure, this can either be a design page with inspirational image/s, or can be an information page or it could be the first product page. This page is part of the spread you will see when you first open the brochure and should entice the customer to want to turn the page to see what else is on offer.
- A spread (Pages 4 and 5) with the LHS page being a full colour insitu inspirational image/s and the RHS page being product information (studio shots) etc. with product names and information.
- A spread (Pages 6 and 7) where there is no full page insitu images used, however both pages are to showcase products and provide the customer with information on sizes, colour options, features and benefits etc.

Any additional pages/designs are welcome to review but a minimum of the above 7 pages are required.
Nice to have
• Full page insitu images on the left hand side page of a spread. This won't be used on all spreads but the aim is to include more insitu inspirational images. Anyway in which these kind of images can be incorporated if not full page are welcomed for review.

Where possible we may reference the insitu image (a,b,c) and list the product details on following product information pages, otherwise the insitu will just be used to give the audience an idea of what you can create and the product information will be included on following pages with studio shots of each item.

An idea is to include callouts on some pages referring customers to the website to look at pricing and further ranges, any ideas welcomed of ways this message can be included inline with a design concept.

We have not supplied any product information or images which are to be used, we are happy to have any images you feel work within your design included and copy doesn't need to be specific but can be repeated generic text.
Should not have
• Please do not include illustrations or cartoon like images, the look and feel should be clean and modern.

```html
<!DOCTYPE html>
<html lang="en">
<head>
<meta charset="utf-8">
<title>Order-In Range Brochure – Page Layouts</title>
<link rel="stylesheet" href="https://fonts.googleapis.com/css2?family=Arimo:wght@400;700&display=swap">
<style>
  :root {
    --orange: #f7941d;
    --orange-dark: #e9830c;
    --white: #ffffff;
    --sheet: #e9e9e9;
    --ink: #333333;
    --muted: #8a8a8a;
    --photo-light: #e6e8ea;
    --photo-mid: #b9bec3;
    --photo-dark: #6f7479;
    --chrome-light: #eef0f2;
    --chrome-mid: #c3c8cd;
    --chrome-edge: #d3d7db;
    --skin: #d9b49a;
  }
  * { margin: 0; padding: 0; box-sizing: border-box; }
  html, body { width: 900px; height: 1200px; overflow: hidden; }
  body {
    background: var(--sheet);
    font-family: "Arimo", Arial, sans-serif;
    color: var(--ink);
    position: relative;
  }
  .spread {
    position: absolute; left: 16px; width: 868px;
    background: var(--white);
    box-shadow: 0 1px 3px rgba(0,0,0,.25);
    overflow: hidden;
  }
  .spread::after {
    content: ""; position: absolute; left: 434px; top: 0; bottom: 0; width: 1px;
    background: rgba(0,0,0,.08);
  }
  .page { position: absolute; top: 0; bottom: 0; width: 434px; }
  .page--left { left: 0; }
  .page--right { left: 434px; }
  .footer-band { position: absolute; left: 0; right: 0; bottom: 0; height: 28px; background: var(--orange); }

  .page-label {
    position: absolute; left: 16px; width: 868px;
    display: flex; justify-content: space-between;
    font-size: 10px; font-weight: 700; color: var(--ink);
  }

  /* Row 1: covers */
  .back-cover { background: var(--orange); }
  .back-cover .brand {
    position: absolute; left: 0; right: 0; top: 116px; text-align: center;
    color: var(--white); font-weight: 700; font-size: 22px;
  }
  .back-cover .fine-print {
    position: absolute; left: 40px; right: 40px; bottom: 22px; text-align: center;
    color: var(--white); font-size: 6px; line-height: 1.6;
  }
  .cover-header {
    position: absolute; left: 0; right: 0; top: 0; height: 100px; background: var(--orange);
  }
  .cover-logo {
    position: absolute; left: 6px; top: 0; width: 138px; height: 58px; background: var(--white);
    color: var(--orange); font-weight: 700; font-size: 20px;
    display: flex; align-items: center; justify-content: center;
  }
  .cover-title {
    position: absolute; left: 158px; top: 14px; color: var(--white);
    font-weight: 700; font-size: 17px; letter-spacing: .2px;
  }
  .cover-subtitle {
    position: absolute; left: 158px; top: 38px; color: var(--white); font-size: 8px;
  }
  .cover-photos { position: absolute; left: 6px; right: 4px; top: 104px; height: 138px; display: flex; gap: 4px; }
  .cover-photos .photo { flex: 1; }
  .photo { background: linear-gradient(160deg, var(--photo-light), var(--photo-mid)); }
  .photo--dark { background: linear-gradient(160deg, var(--photo-mid), var(--photo-dark)); }

  /* Row 2: contents + intro */
  .contents-panel {
    position: absolute; left: 0; top: 0; bottom: 0; width: 234px; background: var(--orange); color: var(--white);
    padding: 22px 16px 0 22px;
  }
  .contents-panel h2 { font-size: 22px; font-weight: 400; margin-bottom: 8px; }
  .contents-list { list-style: none; font-size: 7px; line-height: 1.75; }
  .contents-list li { display: flex; justify-content: space-between; }
  .contents-panel h3 { font-size: 22px; font-weight: 400; margin: 14px 0 6px; }
  .contents-panel p { font-size: 7px; line-height: 1.6; }
  .intro-photo {
    position: absolute; left: 234px; top: 0; bottom: 28px; width: 414px;
    background: linear-gradient(120deg, #f2f2f0 0%, #dcd6cf 45%, var(--skin) 62%, #3f4a6b 100%);
  }
  .intro-quote {
    position: absolute; left: 664px; top: 40px; width: 196px; text-align: right;
    color: var(--orange); font-size: 22px; line-height: 1.2;
  }

  /* Row 3: in-situ + products */
  .insitu-photo {
    position: absolute; left: 0; top: 0; width: 434px; bottom: 28px;
    background: linear-gradient(180deg, #cfd6da 0%, #9ea7ad 45%, #3a3e42 100%);
  }
  .callout { position: absolute; color: var(--white); font-size: 6px; line-height: 1.5; width: 120px; }
  .callout strong { display: block; font-size: 8px; margin-bottom: 2px; }
  .callout::before {
    content: ""; position: absolute; left: -10px; top: 0; bottom: 0; width: 1px; background: var(--white);
  }

  /* Product grid */
  .product-grid {
    position: absolute; left: 16px; right: 16px; top: 16px; bottom: 38px;
    display: grid; grid-template-columns: repeat(3, 1fr); grid-template-rows: 1fr 1fr; gap: 8px 14px;
  }
  .product { display: flex; flex-direction: column; min-height: 0; }
  .product-shot {
    flex: 1; min-height: 0;
    background: linear-gradient(160deg, var(--chrome-light) 0%, var(--chrome-mid) 100%);
    border: 1px solid var(--chrome-edge);
  }
  .product-name {
    background: var(--orange); color: var(--white); font-size: 6px; font-weight: 700;
    padding: 2px 4px; margin-top: 3px; white-space: nowrap;
  }
  .product-desc { font-size: 5px; line-height: 1.5; color: var(--muted); margin-top: 3px; white-space: nowrap; overflow: hidden; }
  .product-meta { display: flex; justify-content: space-between; align-items: center; margin-top: 3px; font-size: 5px; color: var(--ink); }
  .swatches { display: flex; gap: 2px; }
  .swatches span { width: 5px; height: 5px; background: var(--ink); }
  .swatches span:nth-child(2) { background: var(--orange); }
  .swatches span:nth-child(3) { background: #bbbbbb; }
</style>
</head>
<body>

<section class="spread" style="top:16px;height:274px;">
  <div class="page page--left back-cover">
    <div class="brand">LOGO</div>
    <p class="fine-print">Lorem ipsum dolor sit amet consectetur adipiscing elit sed do eiusmod tempor incididunt ut labore et dolore magna aliqua ut enim ad minim veniam quis nostrud exercitation ullamco laboris nisi ut aliquip ex ea commodo consequat</p>
  </div>
  <div class="page page--right">
    <div class="cover-header">
      <div class="cover-logo">LOGO</div>
      <div class="cover-title">TEM SIMINIMAXIM SI AM</div>
      <div class="cover-subtitle">VERO BLACIAS DOLES ET DOLUM AM ESTE OCULPTA PREF</div>
    </div>
    <div class="cover-photos">
      <div class="photo" role="img" aria-label="Modern white kitchen interior"></div>
      <div class="photo photo--dark" role="img" aria-label="Kitchen range hood and appliances"></div>
      <div class="photo" role="img" aria-label="Freestanding white bathtub"></div>
    </div>
    <div class="footer-band"></div>
  </div>
</section>
<div class="page-label" style="top:294px;"><span>Backs Cover</span><span>Front Cover</span></div>

<section class="spread" style="top:316px;height:250px;">
  <div class="contents-panel">
    <h2>Content</h2>
    <ul class="contents-list">
      <li><span>Lorem ipsum dolor sit amet</span><span>1</span></li>
      <li><span>Kitchen taps and mixers</span><span>2</span></li>
      <li><span>Basins and vanity units</span><span>3</span></li>
      <li><span>Baths and shower screens</span><span>4</span></li>
      <li><span>Toilets and accessories</span><span>5</span></li>
      <li><span>Ordering and delivery info</span><span>6</span></li>
    </ul>
    <h3>Make an order</h3>
    <p>Lorem ipsum dolor sit amet, consectetur adipiscing elit sed do eiusmod tempor incididunt ut labore et dolore magna aliqua. Ut enim ad minim veniam quis nostrud.</p>
  </div>
  <div class="intro-photo" role="img" aria-label="Smiling couple embracing in a bright kitchen"></div>
  <div class="intro-quote">Combnent Ehent quatem cus aut volorru ptateni hici-mustia dolorep taturenihit, sit,</div>
  <div class="footer-band"></div>
</section>
<div class="page-label" style="top:580px;"><span>2 Page</span><span>3 Cover</span></div>

<section class="spread" style="top:610px;height:284px;">
  <div class="insitu-photo" role="img" aria-label="Bright bathroom with twin basins and freestanding bath"></div>
  <div class="callout" style="left:56px;top:20px;"><strong>LAM, SECTIA ET</strong>Sed ut perspiciatis unde omnis iste natus error.</div>
  <div class="callout" style="left:332px;top:30px;width:90px;"><strong>LAM, SECTIA ET</strong>Sed ut perspiciatis unde omnis iste.</div>
  <div class="callout" style="left:266px;top:148px;width:90px;"><strong>LAM, SECTIA ET</strong>Nemo enim ipsam voluptatem quia.</div>
  <div class="callout" style="left:66px;top:200px;width:160px;"><strong>LAM, SECTIA ET NEM QUIS</strong>Neque porro quisquam est qui dolorem.</div>
  <div class="page page--right">
    <div class="product-grid">
      <div class="product"><div class="product-shot" role="img" aria-label="Chrome cross-handle basin tap"></div><div class="product-name">LOREM IPSUM DOLOR</div><p class="product-desc">Sed ut perspiciatis unde omnis iste natus</p><div class="product-meta"><span>CODE 1024</span><span class="swatches"><span></span><span></span><span></span></span></div></div>
      <div class="product"><div class="product-shot" role="img" aria-label="Chrome cross-handle basin tap"></div><div class="product-name">LOREM IPSUM DOLOR</div><p class="product-desc">Sed ut perspiciatis unde omnis iste natus</p><div class="product-meta"><span>CODE 1025</span><span class="swatches"><span></span><span></span><span></span></span></div></div>
      <div class="product"><div class="product-shot" role="img" aria-label="Chrome cross-handle basin tap"></div><div class="product-name">LOREM IPSUM DOLOR</div><p class="product-desc">Sed ut perspiciatis unde omnis iste natus</p><div class="product-meta"><span>CODE 1026</span><span class="swatches"><span></span><span></span><span></span></span></div></div>
      <div class="product"><div class="product-shot" role="img" aria-label="Chrome cross-handle basin tap"></div><div class="product-name">LOREM IPSUM DOLOR</div><p class="product-desc">Sed ut perspiciatis unde omnis iste natus</p><div class="product-meta"><span>CODE 1027</span><span class="swatches"><span></span><span></span><span></span></span></div></div>
      <div class="product"><div class="product-shot" role="img" aria-label="Chrome cross-handle basin tap"></div><div class="product-name">LOREM IPSUM DOLOR</div><p class="product-desc">Sed ut perspiciatis unde omnis iste natus</p><div class="product-meta"><span>CODE 1028</span><span class="swatches"><span></span><span></span><span></span></span></div></div>
      <div class="product"><div class="product-shot" role="img" aria-label="Chrome cross-handle basin tap"></div><div class="product-name">LOREM IPSUM DOLOR</div><p class="product-desc">Sed ut perspiciatis unde omnis iste natus</p><div class="product-meta"><span>CODE 1029</span><span class="swatches"><span></span><span></span><span></span></span></div></div>
    </div>
  </div>
  <div class="footer-band"></div>
</section>
<div class="page-label" style="top:900px;"><span>4 Page</span><span>5 Cover</span></div>

<section class="spread" style="top:920px;height:250px;">
  <div class="page page--left">
    <div class="product-grid">
      <div class="product"><div class="product-shot" role="img" aria-label="Chrome cross-handle basin tap"></div><div class="product-name">LOREM IPSUM DOLOR</div><p class="product-desc">Sed ut perspiciatis unde omnis iste natus</p><div class="product-meta"><span>CODE 2011</span><span class="swatches"><span></span><span></span><span></span></span></div></div>
      <div class="product"><div class="product-shot" role="img" aria-label="Chrome cross-handle basin tap"></div><div class="product-name">LOREM IPSUM DOLOR</div><p class="product-desc">Sed ut perspiciatis unde omnis iste natus</p><div class="product-meta"><span>CODE 2012</span><span class="swatches"><span></span><span></span><span></span></span></div></div>
      <div class="product"><div class="product-shot" role="img" aria-label="Chrome cross-handle basin tap"></div><div class="product-name">LOREM IPSUM DOLOR</div><p class="product-desc">Sed ut perspiciatis unde omnis iste natus</p><div class="product-meta"><span>CODE 2013</span><span class="swatches"><span></span><span></span><span></span></span></div></div>
      <div class="product"><div class="product-shot" role="img" aria-label="Chrome cross-handle basin tap"></div><div class="product-name">LOREM IPSUM DOLOR</div><p class="product-desc">Sed ut perspiciatis unde omnis iste natus</p><div class="product-meta"><span>CODE 2014</span><span class="swatches"><span></span><span></span><span></span></span></div></div>
      <div class="product"><div class="product-shot" role="img" aria-label="Chrome cross-handle basin tap"></div><div class="product-name">LOREM IPSUM DOLOR</div><p class="product-desc">Sed ut perspiciatis unde omnis iste natus</p><div class="product-meta"><span>CODE 2015</span><span class="swatches"><span></span><span></span><span></span></span></div></div>
      <div class="product"><div class="product-shot" role="img" aria-label="Chrome cross-handle basin tap"></div><div class="product-name">LOREM IPSUM DOLOR</div><p class="product-desc">Sed ut perspiciatis unde omnis iste natus</p><div class="product-meta"><span>CODE 2016</span><span class="swatches"><span></span><span></span><span></span></span></div></div>
    </div>
  </div>
  <div class="page page--right">
    <div class="product-grid">
      <div class="product"><div class="product-shot" role="img" aria-label="Chrome cross-handle basin tap"></div><div class="product-name">LOREM IPSUM DOLOR</div><p class="product-desc">Sed ut perspiciatis unde omnis iste natus</p><div class="product-meta"><span>CODE 3011</span><span class="swatches"><span></span><span></span><span></span></span></div></div>
      <div class="product"><div class="product-shot" role="img" aria-label="Chrome cross-handle basin tap"></div><div class="product-name">LOREM IPSUM DOLOR</div><p class="product-desc">Sed ut perspiciatis unde omnis iste natus</p><div class="product-meta"><span>CODE 3012</span><span class="swatches"><span></span><span></span><span></span></span></div></div>
      <div class="product"><div class="product-shot" role="img" aria-label="Chrome cross-handle basin tap"></div><div class="product-name">LOREM IPSUM DOLOR</div><p class="product-desc">Sed ut perspiciatis unde omnis iste natus</p><div class="product-meta"><span>CODE 3013</span><span class="swatches"><span></span><span></span><span></span></span></div></div>
      <div class="product"><div class="product-shot" role="img" aria-label="Chrome cross-handle basin tap"></div><div class="product-name">LOREM IPSUM DOLOR</div><p class="product-desc">Sed ut perspiciatis unde omnis iste natus</p><div class="product-meta"><span>CODE 3014</span><span class="swatches"><span></span><span></span><span></span></span></div></div>
      <div class="product"><div class="product-shot" role="img" aria-label="Chrome cross-handle basin tap"></div><div class="product-name">LOREM IPSUM DOLOR</div><p class="product-desc">Sed ut perspiciatis unde omnis iste natus</p><div class="product-meta"><span>CODE 3015</span><span class="swatches"><span></span><span></span><span></span></span></div></div>
      <div class="product"><div class="product-shot" role="img" aria-label="Chrome cross-handle basin tap"></div><div class="product-name">LOREM IPSUM DOLOR</div><p class="product-desc">Sed ut perspiciatis unde omnis iste natus</p><div class="product-meta"><span>CODE 3016</span><span class="swatches"><span></span><span></span><span></span></span></div></div>
    </div>
  </div>
  <div class="footer-band"></div>
</section>
<div class="page-label" style="top:1176px;"><span>6 Page</span><span>7 Cover</span></div>

</body>
</html>
```